Yard Sign Design Needed

Yard sign needed for mowing & landscaping company. Would like to use the top logo with black background which is attached. Would like MOWING to be in large standout letters. The word "landscaping" can be smaller and more artistic or omitted. Will need room for phone number once design is approved. The phone number will need to stand out and look identical/similar to the word 'MOWING"

```html
<!DOCTYPE html>
<html lang="en">
<head>
<meta charset="utf-8">
<title>Norvale Contractors – Mowing Yard Sign</title>
<link rel="stylesheet" href="https://fonts.googleapis.com/css2?family=Montserrat:wght@300;400;600;800&family=Open+Sans:wght@400&display=swap">
<style>
  :root {
    --lime: #97b112;
    --black: #000000;
    --white: #ffffff;
    --backdrop: #d8a469;
  }
  * { margin: 0; padding: 0; box-sizing: border-box; }
  html, body {
    width: 1200px;
    height: 720px;
    overflow: hidden;
    background: var(--backdrop);
  }
  .canvas {
    position: relative;
    width: 1200px;
    height: 720px;
    font-family: "Montserrat", sans-serif;
  }
  .sign-disc {
    position: absolute;
    left: 0;
    top: 0;
  }
  .row {
    position: absolute;
    left: 0;
    width: 1200px;
    display: flex;
    justify-content: center;
    line-height: 1;
  }
  .brand {
    position: absolute;
    left: 0;
    width: 1200px;
    top: 168px;
    display: flex;
    flex-direction: column;
    align-items: center;
    color: var(--lime);
    font-weight: 600;
    line-height: 1;
  }
  .brand-name {
    font-size: 34px;
    letter-spacing: 1px;
  }
  .brand-trade {
    margin-top: 4px;
    font-size: 15px;
    letter-spacing: 0.5px;
  }
  .brand-suffix {
    margin-top: 4px;
    display: flex;
    align-items: center;
    gap: 6px;
    font-size: 8px;
    letter-spacing: 1px;
  }
  .brand-suffix::before,
  .brand-suffix::after {
    content: "";
    width: 60px;
    height: 1px;
    background: var(--lime);
  }
  .service-main {
    top: 272px;
    color: var(--lime);
    font-weight: 800;
    font-size: 88px;
  }
  .service-main span {
    display: inline-block;
    transform: scaleX(1.2);
    letter-spacing: 1px;
  }
  .divider {
    position: absolute;
    left: 431px;
    top: 368px;
    width: 336px;
    height: 2px;
    background: var(--white);
  }
  .service-sub {
    top: 383px;
    left: 346px;
    width: 510px;
    justify-content: space-between;
    color: var(--white);
    font-weight: 300;
    font-size: 33px;
  }
  .phone {
    top: 473px;
    color: var(--lime);
    font-weight: 800;
    font-size: 60px;
    letter-spacing: 0.5px;
  }
  .website {
    top: 539px;
    color: var(--white);
    font-family: "Open Sans", sans-serif;
    font-size: 29px;
  }
</style>
</head>
<body>
  <div class="canvas">
    <svg class="sign-disc" width="1200" height="720" viewBox="0 0 1200 720" aria-hidden="true">
      <circle cx="600" cy="360" r="335" fill="var(--lime)"/>
      <circle cx="600" cy="360" r="326" fill="var(--white)"/>
      <circle cx="600" cy="360" r="319" fill="var(--black)"/>
    </svg>

    <div class="brand">
      <div class="brand-name">NORVALE</div>
      <div class="brand-trade">CONTRACTORS</div>
      <div class="brand-suffix">LLC</div>
    </div>

    <div class="row service-main"><span>MOWING</span></div>
    <div class="divider"></div>
    <div class="row service-sub">
      <span>L</span><span>A</span><span>N</span><span>D</span><span>S</span><span>C</span><span>A</span><span>P</span><span>I</span><span>N</span><span>G</span>
    </div>

    <div class="row phone">0 987 654 320</div>
    <div class="row website">www.norvalecontractors.com</div>
  </div>
</body>
</html>
```